Redesign business cards

We have a new logo and I am not that happy with the layout of our existing card and looking for a change. Font is a bit small and the green can be hard to read. Logo may need a tidy up as the copy I have is not that hi-res too so require you to produce a hi-res version of the logo for us too. There will be three individual business cards to produce with just the names and phone numbers being different. Address will change too, but use what you see on the card for now.

Industry/Entity Type

Business

Requirements
Nice to have
• You could consider a redesign to the new logo, just not too radical. We like the blue and green hexagons as we feel that they are representative of oil industry that we are in.

```html
<!DOCTYPE html>
<html lang="en">
<head>
<meta charset="utf-8">
<title>Verdaline Oil Services – Business Card</title>
<link rel="stylesheet" href="https://fonts.googleapis.com/css2?family=Arimo:wght@400;700&display=swap">
<style>
  :root {
    --backdrop: #3e4b53;
    --card: #ffffff;
    --green: #8cc63f;
    --blue: #29abe2;
    --grey: #8a8a8a;
    --tint-green: rgba(170, 205, 120, .55);
    --tint-blue: rgba(150, 200, 240, .6);
  }
  * { box-sizing: border-box; margin: 0; padding: 0; }
  html, body {
    width: 1200px; height: 1000px; overflow: hidden;
    background: var(--backdrop);
    font-family: "Arimo", Arial, sans-serif;
  }
  .business-card {
    position: absolute; left: 100px; top: 215px;
    width: 1000px; height: 570px;
    background: var(--card);
    overflow: hidden;
  }
  .tint-field {
    position: absolute;
    pointer-events: none;
  }
  .tint-field--top {
    left: -120px; top: -110px; width: 520px; height: 380px;
    background:
      radial-gradient(closest-side, var(--tint-blue) 0%, rgba(150,200,240,0) 60%),
      radial-gradient(closest-side, var(--tint-green) 0%, rgba(170,205,120,.35) 55%, rgba(170,205,120,0) 100%);
  }
  .tint-field--bottom {
    left: 40px; top: 330px; width: 520px; height: 380px;
    background:
      radial-gradient(closest-side, var(--tint-blue) 0%, rgba(150,200,240,0) 60%),
      radial-gradient(closest-side, var(--tint-green) 0%, rgba(170,205,120,.35) 55%, rgba(170,205,120,0) 100%);
  }
  .divider-arc { position: absolute; left: 0; top: 0; }
  .brand {
    position: absolute; left: 55px; top: 262px;
    display: flex; align-items: center; gap: 12px;
  }
  .brand__name {
    font-size: 50px; font-weight: 700; color: var(--green);
    letter-spacing: -1px;
  }
  .brand__dot {
    width: 22px; height: 22px; border-radius: 50%; background: var(--blue);
  }
  .person {
    position: absolute; right: 40px; top: 40px; text-align: right;
  }
  .person__name { font-size: 30px; color: var(--green); }
  .person__credentials { color: var(--blue); }
  .person__role { font-size: 22px; color: var(--grey); margin-top: 4px; }
  .contact {
    position: absolute; left: 470px; top: 290px;
    list-style: none; color: var(--blue); font-size: 26px; line-height: 34px;
  }
  .contact__item { display: flex; align-items: flex-start; }
  .contact__icon { width: 22px; height: 22px; margin: 6px 14px 0 0; flex: none; }
  .contact__address { display: block; font-style: normal; }
</style>
</head>
<body>
  <main class="business-card">
    <div class="tint-field tint-field--top" role="img" aria-label="Faint blue and green hexagon pattern"></div>
    <div class="tint-field tint-field--bottom" role="img" aria-label="Faint blue and green hexagon pattern"></div>

    <svg class="divider-arc" width="1000" height="570" viewBox="0 0 1000 570" aria-hidden="true">
      <circle cx="-40" cy="300" r="440" fill="none" stroke="var(--green)" stroke-width="8"/>
    </svg>

    <div class="brand">
      <span class="brand__dot"></span>
      <span class="brand__name">Verdaline</span>
    </div>

    <header class="person">
      <p class="person__name">Daniel Whitford NZCE <span class="person__credentials">(Mech) P&amp;P</span></p>
      <p class="person__role">Director</p>
    </header>

    <ul class="contact">
      <li class="contact__item">
        <svg class="contact__icon" viewBox="0 0 24 24" aria-hidden="true"><path fill="var(--green)" d="M6.6 10.8a15 15 0 0 0 6.6 6.6l2.2-2.2c.3-.3.7-.4 1-.2 1.1.4 2.3.6 3.6.6.6 0 1 .4 1 1V20c0 .6-.4 1-1 1A17 17 0 0 1 3 4c0-.6.4-1 1-1h3.5c.6 0 1 .4 1 1 0 1.3.2 2.5.6 3.6.1.3 0 .7-.2 1z"/></svg>
        <span>+614 555 01234</span>
      </li>
      <li class="contact__item">
        <svg class="contact__icon" viewBox="0 0 24 24" aria-hidden="true"><rect x="2" y="5" width="20" height="14" fill="var(--green)"/><path d="M2 5l10 8 10-8" fill="none" stroke="#fff" stroke-width="1.6"/></svg>
        <span>daniel@verdaline.co.nz</span>
      </li>
      <li class="contact__item">
        <svg class="contact__icon" viewBox="0 0 24 24" aria-hidden="true"><g fill="none" stroke="var(--green)" stroke-width="1.6"><circle cx="12" cy="12" r="9"/><ellipse cx="12" cy="12" rx="4" ry="9"/><path d="M3 12h18M5 7h14M5 17h14"/></g></svg>
        <span>www.verdaline.com.au</span>
      </li>
      <li class="contact__item">
        <svg class="contact__icon" viewBox="0 0 24 24" aria-hidden="true"><path fill="var(--green)" d="M12 2a7 7 0 0 0-7 7c0 5 7 13 7 13s7-8 7-13a7 7 0 0 0-7-7zm0 9.5A2.5 2.5 0 1 1 12 6.5a2.5 2.5 0 0 1 0 5z"/></svg>
        <address class="contact__address">
          Verdaline Oil Services<br>
          418 Harbour Road<br>
          PO Box 4417<br>
          Eastbrook Queensland 4999
        </address>
      </li>
    </ul>
  </main>
</body>
</html>
```